BrindleStaffing Business Card Design

We are a staffing company finding positions for dedicated nurses and physicians.

Target Market(s)

Business Professionals

Industry/Entity Type

Staffing

Contact Information for Business Card

Gregory Malden
Chairman
417 39th Crescent South
SAINT PETERSBURG FL 33719
813-555-0147 Mobile
813-555-0183 Fax
gmalden@brindlestaffing.example
www.brindlestaffing.example

Font styles to use
Sans Serif

Colors
fbee3e
f04a50
f37122

Requirements
Must have
• Logo Attached, see colors below. We'd like to see Yellow, Orange and Red.

```html
<!DOCTYPE html>
<html lang="en">
<head>
<meta charset="utf-8">
<title>BrindleStaffing Business Card</title>
<link href="https://fonts.googleapis.com/css2?family=Poppins:wght@600&family=Open+Sans:wght@400;700&display=swap" rel="stylesheet">
<style>
  :root {
    --brand-red: #f04a50;
    --brand-orange: #f37122;
    --brand-yellow: #fbee3e;
    --paper: #ffffff;
    --backdrop: #d9d9d9;
    --ink-light: #ffffff;
  }
  * { box-sizing: border-box; margin: 0; padding: 0; }
  html, body {
    width: 1200px; height: 1200px; overflow: hidden;
    background: var(--backdrop);
  }
  .canvas { position: relative; width: 1200px; height: 1200px; }
  .card {
    position: absolute;
    width: 688px; height: 392px;
    overflow: hidden;
    font-family: "Open Sans", sans-serif;
  }
  .card--front { left: 254px; top: 160px; background: var(--paper); }
  .card--back { left: 260px; top: 649px; background: var(--brand-red); }

  .card__wave { position: absolute; inset: 0; width: 100%; height: 100%; }

  .brand-name {
    font-family: "Poppins", sans-serif;
    font-weight: 600;
    letter-spacing: -1px;
    white-space: nowrap;
  }
  .card--front .brand-name {
    position: absolute; left: 46px; top: 52px;
    font-size: 44px; color: var(--brand-red);
  }
  .card--back .brand-name {
    position: absolute; left: 0; right: 0; top: 165px;
    text-align: center;
    font-size: 58px; color: var(--ink-light);
  }

  .person { position: absolute; left: 44px; top: 193px; }
  .person__name { font-size: 22px; font-weight: 700; color: var(--brand-red); line-height: 1.2; }
  .person__title { font-size: 16px; color: var(--brand-orange); line-height: 1.4; }

  .address {
    position: absolute; right: 54px; top: 178px;
    text-align: right; font-style: normal;
    color: var(--ink-light); font-size: 16px; line-height: 23px;
  }
  .contacts {
    position: absolute; right: 64px; top: 253px;
    list-style: none; color: var(--ink-light);
    font-size: 16px; line-height: 23px;
  }
  .contacts__item { display: flex; justify-content: flex-end; align-items: center; gap: 12px; }
  .contacts__icon { width: 16px; height: 16px; flex: none; }
</style>
</head>
<body>
<main class="canvas">

  <section class="card card--front" aria-label="Business card front">
    <svg class="card__wave" viewBox="0 0 550 313" preserveAspectRatio="none" aria-hidden="true">
      <path fill="var(--brand-yellow)" d="M0,207 C110,226 220,203 290,150 C335,118 380,106 420,104 C370,112 330,128 300,160 C230,215 120,232 0,227 Z"/>
      <path fill="var(--brand-red)" stroke="var(--paper)" stroke-width="2" d="M-2,228 C120,232 230,215 300,160 C360,115 440,98 552,98 L552,315 L-2,315 Z"/>
    </svg>

    <div class="brand-name">BrindleStaffing</div>

    <div class="person">
      <p class="person__name">Gregory Malden</p>
      <p class="person__title">Chairman</p>
    </div>

    <address class="address">
      417 39th Crescent South<br>
      SAINT PETERSBURG FL 33719
    </address>

    <ul class="contacts">
      <li class="contacts__item"><span>813-555-0147</span>
        <svg class="contacts__icon" viewBox="0 0 16 16" aria-label="Mobile"><rect x="4" y="1" width="8" height="14" rx="1.5" fill="none" stroke="var(--brand-yellow)" stroke-width="1.5"/><rect x="7" y="12" width="2" height="1.2" fill="var(--brand-yellow)"/></svg></li>
      <li class="contacts__item"><span>813-555-0183</span>
        <svg class="contacts__icon" viewBox="0 0 16 16" aria-label="Fax"><rect x="4" y="1" width="8" height="4" fill="var(--brand-yellow)"/><rect x="1" y="5.5" width="14" height="6" rx="1" fill="var(--brand-yellow)"/><rect x="4" y="10" width="8" height="5" fill="var(--brand-yellow)" stroke="var(--brand-red)" stroke-width="1"/></svg></li>
      <li class="contacts__item"><span>gmalden@brindlestaffing.example</span>
        <svg class="contacts__icon" viewBox="0 0 16 16" aria-label="Email"><rect x="1" y="3" width="14" height="10" fill="var(--brand-yellow)"/><path d="M1,3 L8,9 L15,3" fill="none" stroke="var(--brand-red)" stroke-width="1.2"/></svg></li>
      <li class="contacts__item"><span>www.brindlestaffing.example</span>
        <svg class="contacts__icon" viewBox="0 0 16 16" aria-label="Website"><g fill="none" stroke="var(--brand-yellow)" stroke-width="1.2"><circle cx="8" cy="8" r="6.5"/><ellipse cx="8" cy="8" rx="3" ry="6.5"/><path d="M1.5,8 H14.5 M2.5,4.5 H13.5 M2.5,11.5 H13.5"/></g></svg></li>
    </ul>
  </section>

  <section class="card card--back" aria-label="Business card back">
    <div class="brand-name">BrindleStaffing</div>
  </section>

</main>
</body>
</html>
```